Very new and innovative Web design for Property managers of Vacation rentals

We are looking for a new website design for travel agencies and property managers specialised on vacation rentals business, holiday villas and apartments.

The end users of this website are travellers who are looking for a vacation home for their next holiday: this is the reason why the website must be easy to use, attractive, professional, possibly elegant and focused on get new reservations.

This is a draft of our current website: https://demo5.lunquora.com/
Please consider that we would like to have proposals with a totally different and innovative layout, surprise us!

These are the pages of the website:
• Homepage: feel free to redesign all the homepage as you wish, surprise us with something very new! Please consider that Property manager/Travel agencies usually want to have the opportunity to put in evidence groups of houses with specific characteristics (eg. villas with private swimming pool, apartment in big/small towns, villas with air co, etc…), destinations and tourist areas, and sometimes experiences or activities (please consider that the website layout must be suitable even if some of the previous sections are not used).
• Search page: we’d like to organise the results of the search page in three different ways:
o Grid
o Map
o List
• Property page: to illustrate the characteristics, descriptions, images, …. of the property. It is very important to put in evidence images of the property and to maintain the booking form (and the other call to action bottom – eg. whatsapp) always visible
• Custom pages: static pages composed usually by text, images and call to actions
• Contact us (general form)
• Info request (specific of a property form)
• Booking process
• Blog, organised in four pages:
o Home Page – introduction to the blog
o List of articles
o Single article
o Site Map (presentation of categories and sub-categories)

If possible, we’d prefer to receive the material in Adobe XD or similar so that we can obtain the three versions:
- smartphone
- tablet
- desktop

The website will be then developed in Bootstrap: as a result we’ll need the icons in SVG format (or the library used)

In attachment you can find the map of the website pages

```html
<!DOCTYPE html>
<html lang="en">
<head>
<meta charset="utf-8">
<title>StayNest – Property Policy</title>
<link rel="stylesheet" href="https://fonts.googleapis.com/css2?family=Montserrat:wght@400;500;600&family=Playfair+Display:wght@400;700&display=swap">
<style>
:root{
  --backdrop:#5e7b71;
  --page:#ffffff;
  --brand:#14b98a;
  --ink:#222222;
  --muted:#6b6b6b;
  --footer:#1c1c1c;
  --footer-text:#bdbdbd;
  --serif:"Playfair Display", serif;
  --sans:"Montserrat", sans-serif;
}
*{box-sizing:border-box;margin:0;padding:0}
html,body{width:815px;height:1200px;overflow:hidden}
body{background:var(--backdrop);font-family:var(--sans);color:var(--ink);position:relative}

/* ---------- Desktop page ---------- */
.desktop{position:absolute;left:16px;top:64px;width:700px;height:1172px;background:var(--page);overflow:hidden;transform:scale(.9);transform-origin:0 0}

.site-header{position:relative;height:54px}
.utility-bar{position:absolute;right:0;top:0;height:22px;width:228px;background:var(--brand);
  clip-path:polygon(0 0,100% 0,100% 100%,18px 100%);display:flex;align-items:center;gap:14px;padding-left:34px;
  color:#fff;font-size:6.5px;font-weight:600;letter-spacing:.3px}
.utility-bar span{display:flex;align-items:center;gap:3px}
.brand{position:absolute;left:65px;top:16px;display:flex;align-items:center;gap:6px;font-size:16px;font-weight:500;color:#333}
.brand-mark{width:14px;height:14px;border-radius:50%;background:var(--brand);flex:none}
.main-nav{position:absolute;left:330px;top:34px;display:flex;gap:30px;font-size:7px;font-weight:500;color:#333;letter-spacing:.3px}
.main-nav .active{color:var(--brand)}

.hero{position:relative;height:166px;background:linear-gradient(180deg,#2d3a2f 0%,#3b4336 45%,#2b3226 100%);display:flex;align-items:center;justify-content:center}
.hero h1{font-family:var(--serif);font-weight:700;color:#fff;font-size:25px;letter-spacing:.5px}

.breadcrumb{padding:19px 65px 0;font-size:6.5px;color:var(--muted)}
.breadcrumb b{color:#333;font-weight:500}

.policy-list{padding:18px 65px 0}
.policy-item{display:flex;gap:16px;height:170px}
.policy-photo{width:228px;height:153px;flex:none}
.kicker{font-size:10px;color:#555}
.policy-text h2{font-family:var(--serif);font-weight:400;font-size:24px;line-height:28px;margin-top:4px;color:#222;letter-spacing:.3px}
.policy-text p{font-size:7.5px;line-height:15px;color:var(--muted);margin-top:9px;width:320px}

.photo-night{background:linear-gradient(180deg,#0f1f45 0%,#3b3b52 45%,#b8873a 70%,#3a2a16 100%)}
.photo-tower{background:linear-gradient(180deg,#2f6fd0 0%,#8fb4e8 40%,#e8e3d6 70%,#6a9a3d 100%)}
.photo-pool{background:linear-gradient(180deg,#c9784a 0%,#b08a6a 35%,#4aa3b5 60%,#2b7fa0 100%)}
.photo-arena{background:linear-gradient(180deg,#6f8fc0 0%,#b9c6da 40%,#a0825e 65%,#5c5043 100%)}

.site-footer{position:absolute;left:0;bottom:0;width:700px;height:188px;background:var(--footer);color:var(--footer-text);font-size:7px}
.footer-brand{position:absolute;left:65px;top:72px;display:flex;align-items:center;gap:5px;color:#fff;font-size:12px;font-weight:500}
.footer-brand .brand-mark{width:11px;height:11px}
.footer-col{position:absolute;top:34px}
.footer-col h3{font-family:var(--serif);font-weight:400;color:#fff;font-size:10px;margin-bottom:10px}
.footer-col li{list-style:none;line-height:16px}
.col-links{left:195px}.col-company{left:306px}.col-contact{left:423px}.col-follow{left:578px}
.contact-line{display:flex;gap:5px;align-items:flex-start;margin-bottom:10px;line-height:9px}
.contact-line svg{flex:none;margin-top:1px}
.social{display:flex;align-items:center;gap:5px;margin-bottom:6px}
.social i{width:15px;height:15px;border-radius:50%;background:#fff;display:block;flex:none}
.copyright{position:absolute;left:0;right:0;bottom:32px;text-align:center;font-size:6px}
.copyright b{color:#fff;font-weight:500}

/* ---------- Mobile page ---------- */
.mobile{position:absolute;left:672px;top:18px;width:206px;height:1868px;background:var(--page);overflow:hidden;transform:scale(.62);transform-origin:0 0}
.m-header{height:38px;display:flex;align-items:center;justify-content:center;gap:5px;font-size:14px;font-weight:500;color:#333}
.m-header .brand-mark{width:13px;height:13px}
.m-bar{height:26px;background:var(--brand);display:flex;align-items:center;justify-content:space-between;padding:0 6px;color:#fff;font-size:8px;font-weight:600}
.m-bar-tools{display:flex;align-items:center;gap:6px}
.m-hero{height:48px;background:linear-gradient(180deg,#3f4a52 0%,#4a4f4a 50%,#2f3a3c 100%);display:flex;align-items:center;justify-content:center}
.m-hero h1{font-family:var(--serif);font-weight:700;color:#fff;font-size:8.5px;letter-spacing:.3px}
.m-breadcrumb{height:30px;display:flex;align-items:center;justify-content:center;font-size:8.5px;color:var(--muted)}
.m-breadcrumb b{color:#333;font-weight:500;margin-left:4px}
.m-item{height:287px;padding:0 4px}
.m-photo{width:198px;height:133px}
.m-item .kicker{font-size:7.5px;margin-top:14px}
.m-item h2{font-family:var(--serif);font-weight:400;font-size:14.5px;line-height:19px;margin-top:3px;color:#222}
.m-item p{font-size:6.3px;line-height:12.4px;color:var(--muted);margin-top:6px}
.m-footer{position:absolute;left:0;bottom:0;width:206px;height:578px;background:var(--footer);color:var(--footer-text);padding:20px 4px 0;font-size:9.5px}
.m-footer h3{font-family:var(--serif);font-weight:400;color:#fff;font-size:13px;margin-bottom:12px}
.m-footer ul{margin-bottom:14px}
.m-footer li{list-style:none;line-height:21px}
.m-footer .contact-line{gap:6px;line-height:12px;margin-bottom:14px}
.m-footer .contact-group{margin-bottom:22px}
.m-footer .social{gap:7px;margin-bottom:8px}
.m-footer .social i{width:20px;height:20px}
.m-footer-brand{display:flex;align-items:center;justify-content:center;gap:5px;color:#fff;font-size:13px;font-weight:500;margin-top:34px}
.m-footer-brand .brand-mark{width:12px;height:12px}
.m-copyright{text-align:center;font-size:6.3px;margin-top:6px}
.m-copyright b{color:#fff;font-weight:500}
</style>
</head>
<body>
<main class="desktop">
  <header class="site-header">
    <div class="utility-bar">
      <span><svg width="7" height="7" viewBox="0 0 10 10"><circle cx="5" cy="3.3" r="2.3" fill="none" stroke="#fff"/><path d="M1 10c0-3 8-3 8 0" fill="none" stroke="#fff"/></svg>LOGIN</span>
      <span><svg width="8" height="7" viewBox="0 0 12 10"><path d="M6 9.5L1.2 4.8A2.6 2.6 0 0 1 6 2a2.6 2.6 0 0 1 4.8 2.8z" fill="none" stroke="#fff"/></svg>WHISHLIST</span>
      <span>EN &#709;</span>
    </div>
    <div class="brand"><span class="brand-mark"></span>StayNest</div>
    <nav class="main-nav">
      <span>HOME</span><span>SEARCH</span><span>PROPERTY</span><span class="active">CUSTOM</span><span>CONTACT US</span>
    </nav>
  </header>

  <section class="hero" role="img" aria-label="Dusky photo of a seaside garden with villas and closed parasols">
    <h1>PROPERTY POLICY</h1>
  </section>

  <div class="breadcrumb">Home Page &nbsp;/&nbsp; <b>Property Policy</b></div>

  <section class="policy-list">
    <article class="policy-item">
      <div class="policy-photo photo-night" role="img" aria-label="Night view of a domed basilica and square lit in gold"></div>
      <div class="policy-text">
        <div class="kicker">I must explain to you</div>
        <h2>How all this mistaken idea<br>of &nbsp;Denouncing</h2>
        <p>Nam libero tempore, cum soluta nobis est eligendi optio cumque nihil impedit quo minus id quod maxime placeat facere possimus, omnis voluptas assumenda est, omnis dolor repellendus. Temporibus autem quibusdam et aut officiis debitis aut rerum necessitatibus saepe eveniet ut et voluptates...</p>
      </div>
    </article>
    <article class="policy-item">
      <div class="policy-photo photo-tower" role="img" aria-label="Leaning bell tower and cathedral on a lawn under blue sky"></div>
      <div class="policy-text">
        <div class="kicker">I must explain to you</div>
        <h2>How all this mistaken idea<br>of &nbsp;Denouncing</h2>
        <p>Nam libero tempore, cum soluta nobis est eligendi optio cumque nihil impedit quo minus id quod maxime placeat facere possimus, omnis voluptas assumenda est, omnis dolor repellendus. Temporibus autem quibusdam et aut officiis debitis aut rerum necessitatibus saepe eveniet ut et voluptates...</p>
      </div>
    </article>
    <article class="policy-item">
      <div class="policy-photo photo-pool" role="img" aria-label="Guest relaxing in a hotel swimming pool with tiled walls"></div>
      <div class="policy-text">
        <div class="kicker">I must explain to you</div>
        <h2>How all this mistaken idea<br>of &nbsp;Denouncing</h2>
        <p>Nam libero tempore, cum soluta nobis est eligendi optio cumque nihil impedit quo minus id quod maxime placeat facere possimus, omnis voluptas assumenda est, omnis dolor repellendus. Temporibus autem quibusdam et aut officiis debitis aut rerum necessitatibus saepe eveniet ut et voluptates...</p>
      </div>
    </article>
    <article class="policy-item">
      <div class="policy-photo photo-arena" role="img" aria-label="Ancient stone amphitheatre at dusk"></div>
      <div class="policy-text">
        <div class="kicker">I must explain to you</div>
        <h2>How all this mistaken idea<br>of &nbsp;Denouncing</h2>
        <p>Nam libero tempore, cum soluta nobis est eligendi optio cumque nihil impedit quo minus id quod maxime placeat facere possimus, omnis voluptas assumenda est, omnis dolor repellendus. Temporibus autem quibusdam et aut officiis debitis aut rerum necessitatibus saepe eveniet ut et voluptates...</p>
      </div>
    </article>
  </section>

  <footer class="site-footer">
    <div class="footer-brand"><span class="brand-mark"></span>StayNest</div>
    <div class="footer-col col-links">
      <h3>Quick Links</h3>
      <ul><li>Home</li><li>Search</li><li>Property</li><li>Custom</li><li>Contact Us</li></ul>
    </div>
    <div class="footer-col col-company">
      <h3>Company</h3>
      <ul><li>Privacy Policies</li><li>Reservation Policies</li><li>Cookie Policy</li></ul>
    </div>
    <div class="footer-col col-contact">
      <h3>Contact Us</h3>
      <div class="contact-line"><svg width="6" height="8" viewBox="0 0 6 8"><path d="M3 8C1 5 0 4 0 3a3 3 0 0 1 6 0c0 1-1 2-3 5z" fill="#fff"/><circle cx="3" cy="3" r="1" fill="#1c1c1c"/></svg><span>Via dei Tigli 7 50120<br>Collebello, Firenze (Italy)</span></div>
      <div class="contact-line"><svg width="7" height="7" viewBox="0 0 10 10"><path d="M2 0l2 3-1 1c1 2 2 3 3 3l1-1 3 2-1 2C4 10 0 6 0 1z" fill="#fff"/></svg><span>+39 055 0184720</span></div>
      <div class="contact-line"><svg width="7" height="6" viewBox="0 0 10 8"><rect width="10" height="8" fill="#fff"/><path d="M0 0l5 4 5-4" fill="none" stroke="#1c1c1c"/></svg><span>info@staynest.com</span></div>
    </div>
    <div class="footer-col col-follow">
      <h3>Follow Us</h3>
      <div class="social"><i></i>Friendline</div>
      <div class="social"><i></i>Chirpnet</div>
      <div class="social"><i></i>Snapframe</div>
    </div>
    <div class="copyright">Copyright © 2021 <b>StayNest</b>. All rights reserved.</div>
  </footer>
</main>

<main class="mobile">
  <header class="m-header"><span class="brand-mark"></span>StayNest</header>
  <div class="m-bar">
    <svg width="16" height="11" viewBox="0 0 16 11"><path d="M0 1h16M0 5.5h16M0 10h16" stroke="#fff" stroke-width="1.6"/></svg>
    <div class="m-bar-tools">
      <svg width="9" height="9" viewBox="0 0 10 10"><circle cx="5" cy="3.3" r="2.3" fill="none" stroke="#fff"/><path d="M1 10c0-3 8-3 8 0" fill="none" stroke="#fff"/></svg>
      <svg width="10" height="9" viewBox="0 0 12 10"><path d="M6 9.5L1.2 4.8A2.6 2.6 0 0 1 6 2a2.6 2.6 0 0 1 4.8 2.8z" fill="none" stroke="#fff"/></svg>
      <span>EN &#709;</span>
    </div>
  </div>
  <section class="m-hero" role="img" aria-label="Canal lined with moored boats and old town houses">
    <h1>PROPERTY POLICY</h1>
  </section>
  <div class="m-breadcrumb">Home &nbsp;/ <b>Property Policy</b></div>

  <article class="m-item">
    <div class="m-photo photo-night" role="img" aria-label="Night view of a domed basilica and square lit in gold"></div>
    <div class="kicker">I must explain to you</div>
    <h2>How all this mistaken idea<br>of &nbsp;Denouncing</h2>
    <p>Nam libero tempore, cum soluta nobis est eligendi optio cumque nihil impedit quo minus id quod maxime placeat facere possimus, omnis voluptas assumenda est, omnis dolor repellendus. Temporibus autem quibusdam et aut officiis debitis aut rerum necessitatibus saepe eveniet ut et voluptates...</p>
  </article>
  <article class="m-item">
    <div class="m-photo photo-tower" role="img" aria-label="Leaning bell tower and cathedral on a lawn under blue sky"></div>
    <div class="kicker">I must explain to you</div>
    <h2>How all this mistaken idea<br>of &nbsp;Denouncing</h2>
    <p>Nam libero tempore, cum soluta nobis est eligendi optio cumque nihil impedit quo minus id quod maxime placeat facere possimus, omnis voluptas assumenda est, omnis dolor repellendus. Temporibus autem quibusdam et aut officiis debitis aut rerum necessitatibus saepe eveniet ut et voluptates...</p>
  </article>
  <article class="m-item">
    <div class="m-photo photo-pool" role="img" aria-label="Guest relaxing in a hotel swimming pool with tiled walls"></div>
    <div class="kicker">I must explain to you</div>
    <h2>How all this mistaken idea<br>of &nbsp;Denouncing</h2>
    <p>Nam libero tempore, cum soluta nobis est eligendi optio cumque nihil impedit quo minus id quod maxime placeat facere possimus, omnis voluptas assumenda est, omnis dolor repellendus. Temporibus autem quibusdam et aut officiis debitis aut rerum necessitatibus saepe eveniet ut et voluptates...</p>
  </article>
  <article class="m-item">
    <div class="m-photo photo-arena" role="img" aria-label="Ancient stone amphitheatre at dusk"></div>
    <div class="kicker">I must explain to you</div>
    <h2>How all this mistaken idea<br>of &nbsp;Denouncing</h2>
    <p>Nam libero tempore, cum soluta nobis est eligendi optio cumque nihil impedit quo minus id quod maxime placeat facere possimus, omnis voluptas assumenda est, omnis dolor repellendus. Temporibus autem quibusdam et aut officiis debitis aut rerum necessitatibus saepe eveniet ut et voluptates...</p>
  </article>

  <footer class="m-footer">
    <h3>Quick Links</h3>
    <ul><li>Home</li><li>Search</li><li>Property</li><li>Custom</li><li>Contact Us</li></ul>
    <h3>Company</h3>
    <ul><li>Privacy Policies</li><li>Reservation Policies</li><li>Cookie Policy</li></ul>
    <h3>Contact Us</h3>
    <div class="contact-group">
      <div class="contact-line"><svg width="8" height="10" viewBox="0 0 6 8"><path d="M3 8C1 5 0 4 0 3a3 3 0 0 1 6 0c0 1-1 2-3 5z" fill="#fff"/><circle cx="3" cy="3" r="1" fill="#1c1c1c"/></svg><span>Via dei Tigli 7 50120<br>Collebello, Firenze (Italy)</span></div>
      <div class="contact-line"><svg width="9" height="9" viewBox="0 0 10 10"><path d="M2 0l2 3-1 1c1 2 2 3 3 3l1-1 3 2-1 2C4 10 0 6 0 1z" fill="#fff"/></svg><span>+39 055 0184720</span></div>
      <div class="contact-line"><svg width="9" height="7" viewBox="0 0 10 8"><rect width="10" height="8" fill="#fff"/><path d="M0 0l5 4 5-4" fill="none" stroke="#1c1c1c"/></svg><span>info@staynest.com</span></div>
    </div>
    <h3>Follow Us</h3>
    <div class="social"><i></i>Friendline</div>
    <div class="social"><i></i>Chirpnet</div>
    <div class="social"><i></i>Snapframe</div>
    <div class="m-footer-brand"><span class="brand-mark"></span>StayNest</div>
    <div class="m-copyright">Copyright © 2021 <b>StayNest</b>. All rights reserved.</div>
  </footer>
</main>
</body>
</html>
```